Speech Pathology card for parents of young children

I need a professional, yet fun card for my speech and language pathology services.
I'm trying to offer my speech therapy services to parents of young children. These parents will most likely be women. I want the card to have a fun feel to it and have a concept of speech and language in it (kind of like the cartoon I've attached below showing a boy/girl talking).

I'd want a white background on the card and to bring in some bright colors as well.

Please include the KROV logo in a smaller size on a free corner of the card.

Target Market(s)

parents of young children

Contact Information for Business Card

must have my information and I'd like it to have the KROV logo (small) somewhere in the corner)

Font styles to use
Serif
Sans Serif

Colors

Designer to choose colors to be used in the design.

Requirements
Must have
• The card title should read: Speech-Language Pathologist
• Rosalind Pettry
• MS CCC-SLP/TSSLD (this under the name)
• 415 906 2283
• rosiepettry@kelvormail.net
Nice to have
• i'm looking for a card with a white background and a fun icon that encompasses speaking... similar to the one I've attached.

```html
<!DOCTYPE html>
<html lang="en">
<head>
<meta charset="utf-8">
<title>Rosalind Pettry – Speech-Language Pathologist</title>
<link rel="stylesheet" href="https://fonts.googleapis.com/css2?family=Patrick+Hand+SC&display=swap">
<style>
  :root {
    --page-bg: #d9dadc;
    --card-bg: #ffffff;
    --title-red: #e8343b;
    --name-blue: #1f9fdc;
    --ink: #2b2b2b;
    --accent-orange: #f39200;
    --art-blue: #cfe7f5;
    --art-peach: #f8e3d2;
  }
  * { box-sizing: border-box; margin: 0; padding: 0; }
  html, body {
    width: 1200px; height: 1006px; overflow: hidden;
    background: var(--page-bg);
  }
  body {
    display: flex; align-items: center; justify-content: center;
    font-family: "Patrick Hand SC", "Comic Sans MS", sans-serif;
  }
  .business-card {
    position: relative;
    width: 1000px; height: 572px;
    background: var(--card-bg);
    box-shadow: 0 10px 30px rgba(0,0,0,0.18);
  }
  .card-title {
    position: absolute; left: 80px; top: 150px;
    color: var(--title-red); font-size: 34px; font-weight: 400;
    line-height: 1; white-space: nowrap;
  }
  .practitioner-name {
    position: absolute; left: 96px; top: 240px;
    color: var(--name-blue); font-size: 32px; font-weight: 400;
    line-height: 1; white-space: nowrap;
  }
  .credentials {
    position: absolute; left: 100px; top: 278px;
    color: var(--ink); font-size: 22px; line-height: 1;
  }
  .contact-list {
    position: absolute; left: 110px; top: 330px;
    list-style: none; color: var(--ink); font-size: 22px;
    text-transform: uppercase;
  }
  .contact-list li {
    display: flex; align-items: center; gap: 10px; height: 34px;
    white-space: nowrap;
  }
  .contact-icon { width: 20px; height: 20px; flex: none; }
  .association-mark {
    position: absolute; left: 140px; bottom: 70px;
    display: flex; align-items: center; gap: 12px;
    color: var(--ink); font-size: 26px; line-height: 1;
  }
  .association-dot {
    width: 66px; height: 66px; border-radius: 50%;
    background: var(--ink);
  }
  .speaking-illustration {
    position: absolute; left: 600px; top: 190px;
    width: 280px; height: 270px;
    border-radius: 16px;
    background: linear-gradient(160deg, var(--art-peach) 0%, var(--art-blue) 100%);
  }
</style>
</head>
<body>
  <section class="business-card">
    <h1 class="card-title">Speech-Language Pathologist</h1>
    <h2 class="practitioner-name">Rosalind Pettry</h2>
    <p class="credentials">MS CCC-SLP/TSSLD</p>
    <ul class="contact-list">
      <li>
        <svg class="contact-icon" viewBox="0 0 24 24" aria-hidden="true">
          <path fill="var(--accent-orange)" d="M6.6 10.8a15.1 15.1 0 0 0 6.6 6.6l2.2-2.2a1 1 0 0 1 1-.25 11.4 11.4 0 0 0 3.6.57 1 1 0 0 1 1 1V20a1 1 0 0 1-1 1A17 17 0 0 1 3 4a1 1 0 0 1 1-1h3.5a1 1 0 0 1 1 1c0 1.25.2 2.45.57 3.57a1 1 0 0 1-.25 1z"/>
        </svg>
        <span>415 906 2283</span>
      </li>
      <li>
        <svg class="contact-icon" viewBox="0 0 24 24" aria-hidden="true">
          <rect x="2.5" y="5" width="19" height="14" fill="none" stroke="var(--accent-orange)" stroke-width="2"/>
          <path d="M2.5 5l9.5 8 9.5-8M2.5 19l7-6.5M21.5 19l-7-6.5" fill="none" stroke="var(--accent-orange)" stroke-width="2"/>
        </svg>
        <span>rosiepettry@kelvormail.net</span>
      </li>
    </ul>
    <div class="association-mark">
      <span class="association-dot" aria-hidden="true"></span>
      <span class="association-name">KROV</span>
    </div>
    <div class="speaking-illustration" role="img" aria-label="Cartoon of a cheerful little girl with pigtails, blue top and red skirt, shouting into an orange-striped megaphone"></div>
  </section>
</body>
</html>
```